Book cover for Ink Among Friends by Cedar Hollow Writers' Group

I need a book cover for a book being published by Cedar Hollow Writers' Group.
Text for the book cover is:
Title Ink Among Friends.
Author Cedar Hollow Writers' Group.
Tagline Selected stories, poems, essays other intriguing works.

The book will be printed on 6 x 9 paper.

The book is a collection of stories, essays, poems and pieces collected from the assignments we've completed in the past 18 months. There are contributions from six different writers living in Blue Mountains, ON, Canada.

```html
<!DOCTYPE html>
<html lang="en">
<head>
<meta charset="utf-8">
<title>Ink Among Friends — Cedar Hollow Writers' Group</title>
<link rel="stylesheet" href="https://fonts.googleapis.com/css2?family=Arvo:wght@700&family=Caveat:wght@500&family=Courier+Prime&family=Dancing+Script:wght@500&family=Josefin+Sans:wght@300&family=Roboto+Condensed:wght@500&display=swap">
<style>
  :root {
    --paper-light: #eceeeb;
    --paper-mid: #e2e5e1;
    --paper-dim: #d6d9d5;
    --paper-shade: #c4c7c3;
    --ink-black: #1c1c1c;
    --ink-grey: #5b5b5b;
    --ink-red: #c23a3a;
    --ink-blue: #4b4ba3;
  }
  * { margin: 0; padding: 0; box-sizing: border-box; }
  html, body { width: 836px; height: 1200px; overflow: hidden; background: var(--paper-mid); }
  .cover { position: relative; width: 836px; height: 1200px; overflow: hidden; }
  .paper-stack { position: absolute; inset: 0; width: 836px; height: 1200px; display: block; }
  .sheet { filter: url(#sheet-shadow); }
  .sheet--light { fill: var(--paper-light); }
  .sheet--mid { fill: var(--paper-mid); }
  .sheet--dim { fill: var(--paper-dim); }
  .stack-base { fill: var(--paper-shade); }

  .title { font-weight: normal; }
  .title-word { position: absolute; white-space: nowrap; line-height: 1; transform-origin: left bottom; }
  .title-word--first {
    left: 84px; top: 128px;
    font-family: "Courier Prime", monospace; font-size: 54px; color: var(--ink-black);
    transform: rotate(-15deg);
  }
  .title-word--middle {
    left: 170px; top: 196px;
    font-family: "Dancing Script", cursive; font-size: 80px; color: var(--ink-red);
    transform: rotate(-15deg);
  }
  .title-word--last {
    left: 395px; top: 156px;
    font-family: "Arvo", serif; font-weight: 700; font-size: 96px; color: var(--ink-grey);
    transform: rotate(-17deg);
  }
  .author {
    position: absolute; right: 58px; top: 345px;
    font-family: "Josefin Sans", sans-serif; font-weight: 300; font-size: 40px;
    line-height: 56px; text-align: right; text-transform: uppercase; color: var(--ink-black);
  }
  .tagline {
    position: absolute; left: 200px; top: 572px;
    font-family: "Roboto Condensed", sans-serif; font-weight: 500; font-size: 34px;
    line-height: 52px; color: var(--ink-black);
  }
  .tagline-aside {
    position: absolute; left: 328px; top: 658px;
    font-family: "Caveat", cursive; font-weight: 500; font-size: 24px;
    line-height: 25px; text-align: center; color: var(--ink-blue);
    transform: rotate(-15deg);
  }
</style>
</head>
<body>
  <main class="cover">
    <svg class="paper-stack" viewBox="0 0 900 1286" preserveAspectRatio="none" aria-hidden="true">
      <defs>
        <filter id="sheet-shadow" x="-10%" y="-10%" width="120%" height="120%">
          <feDropShadow dx="-3" dy="4" stdDeviation="3" flood-color="#000" flood-opacity="0.35"/>
        </filter>
      </defs>
      <rect class="stack-base" width="900" height="1286"/>

      <!-- lower sheets -->
      <polygon class="sheet sheet--dim" points="0,1150 175,865 268,865 268,1286 0,1286"/>
      <polygon class="sheet sheet--mid" points="268,860 560,780 430,1286 268,1286"/>
      <polygon class="sheet sheet--light" points="400,1100 610,580 900,640 900,1000 690,1010"/>
      <polygon class="sheet sheet--mid" points="690,1000 900,690 900,960"/>
      <polygon class="sheet sheet--dim" points="430,1115 900,960 900,1286 485,1286"/>

      <!-- upper sheets -->
      <polygon class="sheet sheet--mid" points="0,240 205,240 205,865 0,865"/>
      <polygon class="sheet sheet--light" points="195,540 600,560 545,770 200,872"/>
      <polygon class="sheet sheet--light" points="105,250 360,150 460,470 388,588 42,492"/>
      <polygon class="sheet sheet--light" points="0,0 545,0 560,45 20,268 0,250"/>
      <polygon class="sheet sheet--mid" points="490,0 720,0 670,98"/>
      <polygon class="sheet sheet--light" points="345,150 545,60 900,0 900,300 495,490"/>
      <polygon class="sheet sheet--light" points="550,415 900,265 900,690 705,765"/>
    </svg>

    <h1 class="title">
      <span class="title-word title-word--first">ink</span>
      <span class="title-word title-word--middle">among</span>
      <span class="title-word title-word--last">friends</span>
    </h1>

    <p class="author">Cedar<br>Hollow<br>Writers'<br>Group</p>

    <p class="tagline">Selected stories,<br>poems,<br>essays</p>
    <p class="tagline-aside">&amp; other<br>intriguing<br>works</p>
  </main>
</body>
</html>
```